Design a web site for my business - Brellan Coatworks Mackaby.

We are a family business that handles design, fabrication and installation of powder coated aluminum, stainless steel and glass products. Including handrails, privacy slat screens, electric gates and pool fencing. We are based in the Whitsundays in North Queensland and service an area from Airlie Beach to Townsville.

Target Market(s)

Domestic and commercial

Industry/Entity Type

fabrication - manufacturing

Coding

Coded - Design and coding required

Number of Pages Required

5+ page

Colors
0054AA
0677BA
7BADD7
CADEEF
E8F1F8

Requirements
Must have
• photo galleries, contact page, one page for privacy screens, balustrades, glass fencing, stainless steel handrail, powder coated aluminium handrails and pool fencing

```html
<!DOCTYPE html>
<html lang="en">
<head>
<meta charset="utf-8">
<title>Gallery – Brellan Coatworks Mackaby</title>
<link href="https://fonts.googleapis.com/css2?family=Outfit:wght@300;400;500;600;700&display=swap" rel="stylesheet">
<style>
:root{
  --blue:#0054AA;
  --blue-mid:#0677BA;
  --blue-soft:#7BADD7;
  --blue-pale:#CADEEF;
  --blue-wash:#E8F1F8;
  --page:#F3F6FB;
  --ink:#111418;
  --text:#2a2d33;
  --nav:#4a4d55;
  --placeholder:#D6DDE6;
  --footer:#03234F;
  --footer-text:#b9c6dc;
}
*{box-sizing:border-box;margin:0;padding:0}
html,body{width:1200px;height:2203px;overflow:hidden}
body{background:var(--page);font-family:"Outfit",sans-serif;color:var(--text);position:relative}
.site-header{position:absolute;left:0;top:0;width:1200px;height:84px}
.brand{position:absolute;left:66px;top:26px;display:flex;align-items:center;gap:7px;font-size:13px;font-weight:600;color:var(--nav);line-height:1.2;width:140px}
.brand-mark{width:12px;height:12px;background:var(--nav);flex:none}
.main-nav{position:absolute;right:67px;top:32px;display:flex;gap:38px;font-size:14.5px}
.main-nav a{color:var(--nav);text-decoration:none;position:relative}
.main-nav a.active{font-weight:600;color:#2e3036}
.main-nav a.active::after{content:"";position:absolute;left:-16px;right:-17px;top:47px;height:3px;background:#4a4d55}
.eyebrow{position:absolute;left:0;width:1200px;display:flex;justify-content:center;align-items:center;gap:14px;color:var(--blue);font-weight:500;font-size:15px}
.eyebrow::before{content:"";width:50px;height:1px;background:var(--blue)}
.section-title{position:absolute;left:0;width:1200px;text-align:center;font-weight:600;font-size:39px;line-height:46px;color:var(--ink);letter-spacing:-.3px}
.section-lead{position:absolute;left:0;width:1200px;text-align:center;font-size:19px;line-height:25px;color:#25282e}
.filter-tabs{position:absolute;left:0;top:461px;width:1200px;display:flex;justify-content:center;gap:14px}
.tab{height:42px;padding:0 20px;border-radius:10px;border:1px solid var(--blue-pale);background:var(--blue-wash);color:var(--blue);font-size:14.5px;display:flex;align-items:center}
.tab.active{background:var(--blue);border-color:var(--blue);color:#fff;font-weight:500}
.photo{position:absolute;background:var(--placeholder)}
.btn{position:absolute;top:1640px;height:56px;border-radius:28px;display:flex;align-items:center;justify-content:center;font-size:19px;font-weight:500}
.btn-primary{left:394px;width:225px;background:var(--blue);color:#fff;box-shadow:0 6px 12px rgba(0,84,170,.25)}
.btn-secondary{left:635px;width:169px;background:var(--blue-wash);border:1px solid var(--blue-pale);color:var(--blue)}
.site-footer{position:absolute;left:27px;top:1813px;width:1146px;height:365px;background:var(--footer);border-radius:30px;color:var(--footer-text)}
.footer-brand{position:absolute;left:66px;top:50px;display:flex;align-items:center;gap:7px;color:#fff;font-size:13px;font-weight:600;width:140px;line-height:1.2}
.footer-brand .brand-mark{background:#fff}
.footer-about{position:absolute;left:66px;top:156px;width:270px;font-size:17px;line-height:27px;font-weight:300}
.footer-col{position:absolute;top:50px}
.footer-col h4{color:#fff;font-size:19px;font-weight:600;margin-bottom:17px}
.footer-col li{list-style:none;font-size:15.5px;font-weight:300;line-height:28.5px}
.copyright{position:absolute;left:0;width:100%;top:320px;text-align:center;font-size:15.5px;font-weight:300}
</style>
</head>
<body>
<header class="site-header">
  <div class="brand"><span class="brand-mark"></span>Brellan Coatworks Mackaby</div>
  <nav class="main-nav">
    <a href="#">Home</a><a href="#">About Us</a><a href="#">Our Services</a><a href="#" class="active">Gallery</a><a href="#">Contact Us</a>
  </nav>
</header>

<div class="eyebrow" style="top:199px">Privacy Slat Screens</div>
<h1 class="section-title" style="top:233px">MODERN PRIVACY<br>WITH ARCHITECTURAL STYLE</h1>
<p class="section-lead" style="top:344px">Custom aluminium privacy slat screens designed to enhance security,<br>airflow, and contemporary aesthetics.</p>

<div class="filter-tabs">
  <span class="tab active">Privacy Slat Screens</span>
  <span class="tab">Balustrades</span>
  <span class="tab">Glass Pool Fencing</span>
  <span class="tab">Steel Handrails</span>
  <span class="tab">Aluminium Handrails</span>
  <span class="tab">Pool Fencings</span>
</div>

<div class="photo" role="img" aria-label="Timber-look aluminium slat fence along a concrete path" style="left:66px;top:570px;width:616px;height:333px"></div>
<div class="photo" role="img" aria-label="Charcoal slat privacy screen on a timber deck with outdoor lounge" style="left:698px;top:570px;width:435px;height:333px"></div>
<div class="photo" role="img" aria-label="White slat screens in front of a brick house driveway" style="left:66px;top:920px;width:436px;height:333px"></div>
<div class="photo" role="img" aria-label="Dark grey slat fence around a home with lawn" style="left:518px;top:920px;width:615px;height:333px"></div>

<div class="eyebrow" style="top:1369px">Get In Touch</div>
<h2 class="section-title" style="top:1403px">GET IN TOUCH<br>LET'S BUILD SOMETHING<br>EXCEPTIONAL</h2>
<p class="section-lead" style="top:1553px">Tell us about your project and we'll get back to you with<br>a free, no-obligation quote.</p>
<a class="btn btn-primary">Request Free Quote</a>
<a class="btn btn-secondary">View Projects</a>

<footer class="site-footer">
  <div class="footer-brand"><span class="brand-mark"></span>Brellan Coatworks Mackaby</div>
  <p class="footer-about">Family-owned fabrication<br>of aluminium and stainless steel<br>handrails, glass.</p>
  <div class="footer-col" style="left:430px">
    <h4>SERVICES</h4>
    <ul><li>Glass Balustrades</li><li>Pool Fencing</li><li>Handrails</li><li>Electric Gates</li><li>Slat Screens</li></ul>
  </div>
  <div class="footer-col" style="left:624px">
    <h4>COMPANY</h4>
    <ul><li>About Us</li><li>Our Projects</li><li>Request a Quote</li><li>Service Areas</li></ul>
  </div>
  <div class="footer-col" style="left:818px">
    <h4>CONTACT</h4>
    <ul><li>0700 000 000</li><li>info@brellancoatworks.com.au</li><li>Mon–Fri: 7am – 4pm</li><li>Sat: By appointment</li></ul>
  </div>
  <p class="copyright">© 2026 Brellan Coatworks Mackaby. All rights reserved - Designed &amp; Developed by Lumen Studio</p>
</footer>
</body>
</html>
```